Lumo Vance IT company Soho london Stationary

We've just had a new logo designed on Gallow Pier and we now need some Stationary to go with it.
We're a small IT support firm supporting Design companies in Soho London. Most of our clients work on Vorls and a relatively creative so we want a relatively informal design on our stationary to reflect this.
We'd like to stick with the green in the logo but we're not adverse to adding another few colours to the palette.
Please see the attached file for our logo and not our website.

It Company

```html
<!DOCTYPE html>
<html lang="en">
<head>
<meta charset="utf-8">
<title>Lumo Vance – Business Card</title>
<link rel="stylesheet" href="https://fonts.googleapis.com/css2?family=Mulish:wght@400;700;800&display=swap">
<style>
  :root {
    --lime: #b4d334;
    --lime-dark: #9dbb22;
    --ink: #232323;
    --card-black: #1a1a1a;
    --paper: #ffffff;
    --muted: #9a9a9a;
    --backdrop: #ece9e4;
  }
  * { box-sizing: border-box; margin: 0; padding: 0; }
  html, body {
    width: 1200px; height: 900px; overflow: hidden;
    background: var(--backdrop);
    font-family: "Mulish", sans-serif;
  }
  .canvas { position: relative; width: 1200px; height: 900px; }

  .card {
    position: absolute;
    width: 560px; height: 340px;
    border-radius: 4px;
    overflow: hidden;
    box-shadow: 0 6px 18px rgba(0,0,0,0.18);
  }

  /* Back of card */
  .card-back { left: 110px; top: 70px; background: var(--card-black); }
  .card-back .web {
    position: absolute; right: 34px; bottom: 30px;
    font-size: 19px; color: #c9c9c9; letter-spacing: 0.3px;
  }
  .card-back .web strong { color: var(--lime); font-weight: 700; }

  /* Front of card */
  .card-front { left: 530px; top: 480px; background: var(--paper); }
  .front-top {
    position: absolute; left: 0; top: 0; width: 100%; height: 158px;
    display: flex; align-items: center; justify-content: center; gap: 14px;
  }
  .brand-dot {
    width: 20px; height: 20px; border-radius: 50%; background: var(--lime);
  }
  .brand-name {
    font-size: 52px; font-weight: 800; color: var(--lime);
    letter-spacing: -0.5px;
  }
  .divider {
    position: absolute; left: 0; top: 158px; width: 100%; height: 3px;
    background: var(--ink);
  }
  .front-band {
    position: absolute; left: 0; top: 161px; width: 100%; height: 179px;
    background: var(--lime);
  }
  .contact {
    position: absolute; left: 36px; top: 28px;
    color: var(--ink); font-size: 15px; line-height: 1.35;
  }
  .contact .address { font-weight: 700; margin-bottom: 16px; }
  .contact .line { font-weight: 400; }
  .contact .label {
    display: inline-block; width: 16px; color: var(--paper); font-weight: 800;
  }
  .person {
    position: absolute; right: 200px; top: 22px; text-align: right; color: var(--ink);
  }
  .person .name { font-size: 22px; font-weight: 700; }
  .person .role { font-size: 14px; font-weight: 400; margin-top: 2px; }
</style>
</head>
<body>
<main class="canvas">

  <section class="card card-back" aria-label="Business card, back">
    <p class="web">http://<strong>lumo-vance</strong>.it</p>
  </section>

  <section class="card card-front" aria-label="Business card, front">
    <header class="front-top">
      <span class="brand-dot" aria-hidden="true"></span>
      <span class="brand-name">Lumo Vance</span>
    </header>
    <div class="divider"></div>
    <div class="front-band">
      <div class="contact">
        <p class="address">42 Carrow Lane<br>London W9Z 2QX</p>
        <p class="line"><span class="label">P</span>(123) 456 7890</p>
        <p class="line"><span class="label">F</span>(123) 456 7890</p>
        <p class="line"><span class="label">E</span>info@lumo-vance.it</p>
      </div>
      <div class="person">
        <p class="name">Your Name</p>
        <p class="role">Position</p>
      </div>
    </div>
  </section>

</main>
</body>
</html>
```